Belle Lueur Hand Crafted Candles promotional flyer

Hand Crafted Soy Candles - I need a flyer to promote my candles and to give information on care of candles.I want this to use the design and colours I already have for my labels and the photo I have attached.I am aiming at a sophisticated market so would like to reflect this in the design.
Should appeal to sophisticated women who enjoy the pleasure of candles - to enhance their enjoyment of life - gives them the 'joie de vivre'.
the candles are hand crafted from all natural ingredients, environmentally friendly and with exquisite fragrances

Target Market(s)

sophisticated females

Industry/Entity Type

Promotional

Font styles to use
Script

Colors
cfeae6
ecdaeb

Requirements
Must have
• something expressing 'joie de vivre' - the enjoyment of candles
Should not have
• bright colours

```html
<!DOCTYPE html>
<html lang="en">
<head>
<meta charset="utf-8">
<title>Belle Lueur Hand Crafted Candles – Flyer</title>
<link rel="stylesheet" href="https://fonts.googleapis.com/css2?family=Pinyon+Script&family=Parisienne&display=swap">
<style>
  :root {
    --bg-top: #1c2221;
    --bg-mid: #3a4240;
    --bg-low: #4d5553;
    --ink: #eef2f1;
    --ink-soft: #d6dddb;
    --dot: #ecdaeb;
    --mint: #cfeae6;
    --rule: #c9d0ce;
    --banner-edge: #8a827c;
  }
  * { margin: 0; padding: 0; box-sizing: border-box; }
  html, body { width: 850px; height: 1200px; overflow: hidden; background: var(--bg-top); }
  .flyer {
    position: relative; width: 850px; height: 1200px; overflow: hidden;
    background: linear-gradient(180deg, var(--bg-top) 0%, #262d2c 30%, var(--bg-mid) 60%, var(--bg-low) 100%);
    color: var(--ink);
    font-family: "Parisienne", cursive;
  }
  .backdrop-photo {
    position: absolute; left: 60px; top: 150px; width: 780px; height: 420px;
    background: radial-gradient(ellipse at 30% 60%, rgba(150,160,158,.28), transparent 60%),
                radial-gradient(ellipse at 75% 55%, rgba(120,130,140,.22), transparent 55%);
  }
  .bottom-waves { position: absolute; left: 0; bottom: 0; width: 850px; height: 260px; }

  .banner { position: absolute; left: 60px; top: 50px; width: 730px; height: 56px; }
  .title {
    position: absolute; left: 0; right: 0; top: 50px; text-align: center;
    font-family: "Pinyon Script", cursive; font-size: 46px; line-height: 56px; font-weight: 400; color: var(--ink);
  }

  .features {
    position: absolute; left: 96px; top: 176px; width: 390px; list-style: none;
    font-family: "Pinyon Script", cursive; font-size: 28px; line-height: 26px; color: var(--ink);
  }
  .features li { position: relative; padding-left: 22px; margin-bottom: 5px; }
  .features li::before {
    content: ""; position: absolute; left: 0; top: 10px; width: 7px; height: 7px;
    border-radius: 50%; background: var(--ink);
  }

  .hero-photo {
    position: absolute; left: 544px; top: 232px; width: 180px; height: 232px;
    border-radius: 30px;
    background: radial-gradient(ellipse 42% 40% at 50% 50%, #f1f3f2 0%, #d6dcdb 90%, #1d2226 100%),
                #14181c;
    box-shadow: 0 0 28px 8px rgba(220,230,228,.35);
  }

  .section-title {
    position: absolute; font-family: "Pinyon Script", cursive; font-weight: 400; color: var(--ink);
    border-bottom: 1.5px solid var(--rule); padding-bottom: 2px;
  }
  .soy-title { left: 80px; top: 556px; width: 228px; font-size: 28px; line-height: 30px; padding-left: 16px; }
  .refill-title { left: 80px; top: 784px; width: 272px; font-size: 28px; line-height: 30px; padding-left: 12px; }
  .care-title {
    left: 438px; top: 556px; width: 362px; font-size: 21px; line-height: 19px;
    padding-left: 16px; padding-right: 70px; padding-bottom: 6px;
  }

  .notes { position: absolute; list-style: none; font-size: 13px; line-height: 15px; color: var(--ink-soft); }
  .notes li { position: relative; padding-left: 18px; margin-bottom: 11px; }
  .notes li::before {
    content: ""; position: absolute; left: 2px; top: 4px; width: 7px; height: 7px;
    border-radius: 50%; background: var(--dot);
  }
  .soy-notes { left: 72px; top: 596px; width: 290px; }
  .refill-notes { left: 72px; top: 826px; width: 290px; }
  .care-notes { left: 428px; top: 642px; width: 362px; font-size: 13px; line-height: 15.5px; }
  .care-notes li { margin-bottom: 8px; }

  .double-rule { position: absolute; left: 72px; top: 934px; width: 236px; height: 6px;
    border-top: 1.5px solid var(--rule); border-bottom: 1.5px solid var(--rule); }
  .contact { position: absolute; left: 90px; top: 948px; width: 320px; font-size: 16px; line-height: 16px; color: var(--ink-soft); }
  .contact .lines { margin-top: 8px; font-size: 18px; line-height: 19px; }
  .care-rule { position: absolute; left: 438px; top: 1052px; width: 362px; border-top: 1.5px solid var(--rule); }

  .brand-seal {
    position: absolute; left: 90px; top: 1074px; width: 64px; height: 64px; border-radius: 50%;
    background: #f2f4f3; display: flex; align-items: center; justify-content: center; text-align: center;
    font-family: "Pinyon Script", cursive; font-size: 14px; line-height: 14px; color: #3b4548;
  }
  .range-photo {
    position: absolute; left: 296px; top: 1080px; width: 300px; height: 62px; border-radius: 4px;
    background: linear-gradient(90deg, #2d3b8a 0 6%, #e8e3d6 10% 24%, #cfcbc0 28% 36%, #101214 40% 60%, #d8d4ca 64% 80%, #e8e3d6 84% 92%, #2d3b8a 95%);
    opacity: .9;
  }
</style>
</head>
<body>
<main class="flyer">
  <div class="backdrop-photo" role="img" aria-label="Soft-focus photo of soy candles in glass jars on a table"></div>

  <svg class="bottom-waves" viewBox="0 0 850 260" aria-hidden="true">
    <path d="M0 150 C120 110 210 190 330 170 C450 150 520 120 640 150 C740 175 800 150 850 140 L850 260 L0 260 Z" fill="#6b7371" opacity=".55"/>
    <path d="M0 200 C140 170 260 240 420 215 C560 195 680 215 850 190 L850 260 L0 260 Z" fill="#8a918f" opacity=".45"/>
  </svg>

  <svg class="banner" viewBox="0 0 730 56" aria-hidden="true">
    <defs>
      <linearGradient id="bannerFill" x1="0" y1="0" x2="0" y2="1">
        <stop offset="0" stop-color="#6a645f"/><stop offset="1" stop-color="#3e3935"/>
      </linearGradient>
    </defs>
    <path d="M40 8 L690 8 C705 8 712 28 712 28 C712 28 705 50 690 50 L40 50 C25 50 18 28 18 28 C18 28 25 8 40 8 Z"
          fill="url(#bannerFill)" stroke="var(--banner-edge)" stroke-width="1.5"/>
  </svg>
  <h1 class="title">Belle Lueur</h1>

  <ul class="features">
    <li>Belle Lueur – an exuberant enjoyment of life – these candles will fill you with pure delight.</li>
    <li>Candles are lovingly hand-poured and use only the finest of ingredients and fragrances</li>
    <li>Hand crafted soy candle creations</li>
    <li>Completely non-toxic</li>
    <li>Exquisite fragrances</li>
    <li>Clean burning</li>
    <li>Environmentally friendly.</li>
  </ul>

  <div class="hero-photo" role="img" aria-label="Photo of a black glass jar soy candle with a white oval label"></div>

  <h2 class="section-title soy-title">Why soy wax?</h2>
  <ul class="notes soy-notes">
    <li>Soft smooth wax that burns<br>clear – no soot or smoke</li>
    <li>Soy wax candles burn up to 50%<br>longer than traditional paraffin candles</li>
    <li>Made from soya beans, a renewable natural resource that supports and sustains agriculture – it is biodegradable and environmentally friendly</li>
    <li>Soy wax burns cooler than paraffin<br>and disperses the fragrance more fully</li>
  </ul>

  <h2 class="section-title refill-title">Containers can be refilled</h2>
  <ul class="notes refill-notes">
    <li>I offer a refill service – if you return your containers to me I can refill with the fragrance of your choice</li>
    <li>Or if you have a special container<br>you would like to use for your candle<br>just contact me for a quote</li>
  </ul>

  <div class="double-rule"></div>
  <div class="contact">
    <p>I have a wide range of fragrances<br>– please contact me for details:</p>
    <p class="lines">Email: hello@belleleurcandles.co.nz<br>Mobile: 021 555 0148<br>Website: www.belleleurcandles.co.nz</p>
  </div>

  <h2 class="section-title care-title">How to care for your candle – the following tips will ensure you have a long lasting, fully fragranced candle</h2>
  <ul class="notes care-notes">
    <li>When lighting your candle for the first time, allow the wax to melt all the way to the sides of the container – this creates a 'memory' and avoids 'tunnelling' as the candle burns</li>
    <li>Always trim the wick to about 6-8mm before re-lighting your candle. This will ensure a long lasting candle, minimise soot and remove any mushrooming of the wick from a previous burn</li>
    <li>It is preferable to use a candle 'snuffer' to extinguish the flame, or a lid if the candle has one. Alternatively, you can dip the wick into the melted wax and then straighten. This will stop the wick from smoking and help with relighting</li>
    <li>All Belle Lueur candles are hand poured not mass produced – although every effort is made to ensure consistency, every candle may be different</li>
    <li>Sometimes you may notice darker patches or wet spots – this is not a fault, it is just the natural way the wax has set – it does not affect the candle in any way</li>
    <li>The top of the candle may also appear slightly uneven – this is just a sign of natural soy wax being hand poured</li>
    <li>Do not leave your candle in the sunlight as it may turn a yellow colour – again this does not affect the candle in any way – it just loses its creamy white colour</li>
    <li>As these candles contain no preservatives or chemicals it is recommended that they should be used within 6 months</li>
  </ul>
  <div class="care-rule"></div>

  <div class="brand-seal">Belle<br>Lueur</div>
  <div class="range-photo" role="img" aria-label="Photo of the full candle range in blue, white and black jars in a row"></div>
</main>
</body>
</html>
```